Word Bureau Ostrelle Templates

We run a large number of businesses, including schools, airports, hotels and offices. We write reports on a daily basis and are looking for a strong and sexy WORD Template. We already have a logo in place (see graphical chart attached), that is rights' protected. We are looking for a beautiful wich reflect modern design and human aspects. Our logo has 2 design, full fill and watermark. It can be used in red or black.

Architects, Fire brigade, Building investors, contactors

• Arial, Calibri, ...

• Cover page, summary, Bullet points, Tables, Figures, Annex

```html
<!DOCTYPE html>
<html lang="en">
<head>
<meta charset="utf-8">
<title>Bureau Ostrelle – Report Cover</title>
<link href="https://fonts.googleapis.com/css2?family=Open+Sans:wght@400;600&display=swap" rel="stylesheet">
<style>
  :root {
    --backdrop: #d9dcdd;
    --cover-dark: #050505;
    --cover-mid: #151515;
    --cover-light: #6e6e6e;
    --accent-red: #e33a33;
    --edge-grey: #9a9a9a;
    --band-dark: #1b1b1b;
    --text-white: #ffffff;
  }
  * { margin: 0; padding: 0; box-sizing: border-box; }
  html, body {
    width: 1200px;
    height: 784px;
    overflow: hidden;
    background: var(--backdrop);
    font-family: "Open Sans", Arial, sans-serif;
  }
  .canvas {
    width: 1200px;
    height: 784px;
    display: flex;
    align-items: center;
    justify-content: center;
  }
  .cover {
    position: relative;
    width: 525px;
    height: 742px;
    background: linear-gradient(215deg, var(--cover-light) 0%, #3a3a3a 28%, var(--cover-mid) 55%, var(--cover-dark) 100%);
    box-shadow: 0 6px 22px rgba(0,0,0,0.18);
    overflow: hidden;
  }
  .watermark-disc {
    position: absolute;
    left: 70px;
    top: 110px;
    width: 420px;
    height: 420px;
    border-radius: 50%;
    background: linear-gradient(200deg, rgba(255,255,255,0.10) 0%, rgba(255,255,255,0.04) 45%, rgba(0,0,0,0.35) 100%);
  }
  .brand {
    position: absolute;
    left: 150px;
    top: 268px;
    display: flex;
    align-items: flex-start;
    gap: 16px;
  }
  .brand-dot {
    flex: none;
    width: 40px;
    height: 40px;
    border-radius: 50%;
    background: var(--accent-red);
    margin-top: 8px;
  }
  .brand-name {
    color: var(--text-white);
    font-weight: 600;
    font-size: 46px;
    line-height: 1.08;
    letter-spacing: 0.5px;
  }
  .footer-url {
    position: absolute;
    left: 26%;
    width: 34%;
    bottom: 30px;
    text-align: center;
    color: var(--text-white);
    font-size: 13px;
    font-weight: 600;
    letter-spacing: 0.6px;
  }
  .footer-band {
    position: absolute;
    left: 0;
    right: 0;
    bottom: 0;
    height: 14px;
    display: flex;
  }
  .footer-band .edge { flex: 26; background: var(--band-dark); border-top: 2px solid var(--edge-grey); }
  .footer-band .accent { flex: 34; background: var(--accent-red); }
  .footer-band .edge-end { flex: 40; background: var(--band-dark); border-top: 2px solid var(--edge-grey); }
</style>
</head>
<body>
  <main class="canvas">
    <section class="cover">
      <div class="watermark-disc" role="img" aria-label="Large faint brand watermark area"></div>
      <div class="brand">
        <span class="brand-dot"></span>
        <h1 class="brand-name">Bureau<br>Ostrelle</h1>
      </div>
      <p class="footer-url">www.example.com</p>
      <div class="footer-band">
        <span class="edge"></span>
        <span class="accent"></span>
        <span class="edge-end"></span>
      </div>
    </section>
  </main>
</body>
</html>
```